Review/Re-Design Supermarket E-Commerce website

We have launched our Supermarket E-commerce Website but feel it is lacking a modern feel.

Please re-design the current Supermarket E-commerce site, creating a more modern look and feel.

I am looking for design changes to things such as:

- Fonts
- Button shape & Size
- Shapes of boxes
- Layout of drop down menus
- A new shopping cart / button
- The Header (and in particular the use and positioning of the logo)
- Supplying a generic background image (currently berries)

Please do not change the structure of the page. For instance, the category selection will always be on the left, the items will always be displayed in rows of 3 and the shopping cart should be on the right.
Updates

Current site can be found at www.brovanmarket.com.au

Project Deadline Extended
Reason: designs coming in are generally too different from current design. we are looking for less that 10% change to the overall look and feel. one aspect that needs a lot of work is the checkout cart on the right hand side. please checkout http://www2.pelkinfreshmart.com.au/?gclid=QXRP4kdmwnLBHTYEzJuaPGEKtB

Target Market(s)

Consumers buying their weekly grocery shopping online

Industry/Entity Type

Shopping

Number of Pages Required

1 page

Requirements
Must have
• Stick to the branding of the Logo. Which is Red, Blue and White.
• Other colours may be used in small percentages.
Should not have
• Do not change the Structure of the site.

```html
<!DOCTYPE html>
<html lang="en">
<head>
<meta charset="utf-8">
<title>Brovan Market – Apples</title>
<link rel="stylesheet" href="https://fonts.googleapis.com/css2?family=Lato:wght@400;700&family=Arimo:wght@400;700&display=swap">
<style>
:root{
  --blue:#0b5cb5;
  --red:#e5252b;
  --orange:#e8571c;
  --page:#d4cbc4;
  --bar:#ece7e2;
  --footer:#ede7e2;
  --side:#f7f7f7;
  --line:#d9d4cf;
  --ink:#333;
  --muted:#666;
}
*{box-sizing:border-box;margin:0;padding:0}
html,body{width:1120px;height:1200px;overflow:hidden}
body{background:var(--page);font-family:"Lato",sans-serif;color:var(--ink);position:relative}
.scene-left,.scene-right{position:absolute;top:0;height:326px;width:175px;
  background:radial-gradient(circle at 45% 40%,#e9c88a 0%,#b9774a 35%,#3f5c3e 75%,#2e4a33 100%)}
.scene-left{left:0}
.scene-right{right:0;width:177px;background:radial-gradient(circle at 55% 35%,#f1dcae 0%,#c89b62 40%,#8a5b3b 70%,#3a5a3c 100%)}
.site{position:absolute;left:175px;top:0;width:768px;height:1200px;background:#fff}
.topbar{height:34px;background:var(--bar);display:flex;align-items:center;justify-content:space-between;padding:0 21px 0 9px;font-family:"Arimo",sans-serif;font-size:10px}
.topbar .phone{display:flex;align-items:center;gap:5px}
.topbar nav{display:flex;gap:12px}
.topbar nav a{color:var(--ink);text-decoration:none}
.topbar nav a.register{color:var(--red)}
.header{position:relative;height:66px;border-bottom:2px solid var(--blue)}
.logo{position:absolute;left:10px;top:20px;display:flex;align-items:center;gap:8px}
.logo .mark{width:20px;height:20px;background:var(--red);border-radius:50%}
.logo span{font-family:"Lato",sans-serif;font-weight:700;font-size:20px;color:var(--blue);letter-spacing:.5px}
.search{position:absolute;left:302px;top:22px;display:flex;height:25px}
.search .field{width:238px;border:1px solid #ccc;display:flex;align-items:center;justify-content:space-between;padding:0 10px 0 12px;font-size:10.5px;color:#777}
.search .field b{font-weight:400;color:#444;font-size:9.5px;display:flex;align-items:center;gap:8px}
.search button{width:29px;border:0;background:var(--orange);display:flex;align-items:center;justify-content:center}
.navrow{position:relative;height:36px;border-bottom:2px solid #e2e2e2}
.shopby{position:absolute;left:0;top:0;width:144px;height:36px;background:var(--blue);color:#fff;font-weight:700;font-size:11.5px;padding:12px 14px}
.tabs{position:absolute;left:144px;top:0;height:36px;display:flex}
.tabs a{display:flex;align-items:center;gap:5px;padding:0 14px;font-size:11.5px;color:var(--ink);text-decoration:none;border-right:1px solid #e2e2e2}
.tabs a .ic{color:var(--blue);font-size:11px}
.sidebar{position:absolute;left:0;top:138px;width:144px;height:832px;background:var(--side);border-right:2px solid #e9e9e9;padding-top:4px}
.sidebar li{list-style:none;height:24px;display:flex;align-items:center;justify-content:space-between;padding:0 10px 0 11px;font-size:9.5px;color:#444}
.sidebar li::after{content:">";font-size:8px;color:#999}
.crumbs{position:absolute;left:162px;top:153px;font-size:11px;color:#666;display:flex;gap:9px}
.crumbs .sep{font-size:8px;line-height:14px}
.crumbs .here{color:var(--red)}
.card{position:absolute;width:150px;height:261px;border:1px solid var(--line);background:#fff}
.card .photo{position:absolute;left:19px;top:22px;width:112px;height:112px;border-radius:50%;
  background:radial-gradient(circle at 40% 35%,#f25b5f 0%,#d11b24 45%,#8f0d14 100%)}
.card .title{position:absolute;left:0;right:0;top:145px;text-align:center;font-size:11.5px}
.card .title small{font-size:9px;color:#666;margin-left:6px}
.card .price{position:absolute;left:0;right:0;top:163px;text-align:center;color:var(--red);font-size:11.5px}
.qty{position:absolute;left:10px;top:210px;display:flex;align-items:center;gap:9px;font-size:11px}
.qty i{width:12px;height:12px;border-radius:50%;border:1px solid #bbb;background:#eee;font-style:normal;font-size:9px;line-height:10px;text-align:center;color:#555}
.add{position:absolute;left:75px;top:206px;width:61px;height:24px;border:0;background:var(--orange);color:#fff;font-family:"Arimo",sans-serif;font-size:11.5px}
.cart{position:absolute;left:640px;top:179px;width:118px;height:243px;background:#eeeae7;border:1px solid var(--line)}
.cart .basket{position:absolute;left:10px;top:20px}
.cart .items{position:absolute;left:10px;top:48px;font-size:10.5px;color:#555}
.cart .sub{position:absolute;right:10px;top:20px;text-align:left;font-size:10.5px;color:#555}
.cart .sub b{display:block;font-weight:400;font-size:13px;color:var(--ink)}
.checkout{position:absolute;left:17px;top:78px;width:88px;height:27px;border:0;background:var(--blue);color:#fff;font-family:"Lato",sans-serif;font-weight:700;font-size:11.5px}
.cart hr{position:absolute;left:0;right:0;top:123px;border:0;border-top:1px solid #d6d0ca}
.collect{position:absolute;left:9px;top:137px;right:4px}
.collect .row{display:flex;align-items:center;gap:6px;font-size:11.5px;color:#444}
.collect p{font-size:8.8px;color:#555;line-height:14px;margin:6px 0 14px 1px}
.footer{position:absolute;left:0;top:970px;width:768px;height:230px;background:var(--footer)}
.footer h4{position:absolute;font-weight:400;font-size:11.5px;color:#333}
.store{position:absolute;top:47px;height:37px;background:#111;color:#fff;display:flex;align-items:center;justify-content:center;gap:7px;font-size:15px}
.store .sq{width:16px;height:16px;border-radius:50%;background:#fff}
.pay{position:absolute;top:148px;font-size:15px;font-weight:700;display:flex;align-items:center}
.flinks{position:absolute;top:54px;list-style:none}
.flinks li{font-size:9.5px;color:#555;height:24px}
.divider{position:absolute;left:436px;top:52px;height:148px;border-left:1px solid #d2ccc6}
.contact-phone{position:absolute;left:641px;top:50px;font-size:9.5px;color:#555}
.social{position:absolute;top:94px;width:24px;height:24px;border-radius:50%}
</style>
</head>
<body>
<div class="scene-left" role="img" aria-label="Seafood pasta dish on a green tablecloth"></div>
<div class="scene-right" role="img" aria-label="Fresh bread and seafood on a table"></div>

<div class="site">
  <div class="topbar">
    <div class="phone">
      <svg width="13" height="13" viewBox="0 0 24 24" fill="none" stroke="#999" stroke-width="2"><path d="M5 3h4l2 5-3 2a11 11 0 0 0 6 6l2-3 5 2v4a2 2 0 0 1-2 2A17 17 0 0 1 3 5a2 2 0 0 1 2-2z"/></svg>
      <span>1300 555 019</span>
    </div>
    <nav><a href="#">Products</a><a href="#">Login</a><a href="#" class="register">Register</a><a href="#">My Cart</a></nav>
  </div>

  <header class="header">
    <div class="logo"><div class="mark"></div><span>BROVAN MARKET</span></div>
    <div class="search">
      <div class="field">Search for <b>House Range <svg width="8" height="6"><path d="M0 0h8L4 6z" fill="#444"/></svg></b></div>
      <button aria-label="Search"><svg width="15" height="15" viewBox="0 0 24 24" fill="none" stroke="#fff" stroke-width="3"><circle cx="14" cy="10" r="7"/><path d="M9 15l-6 6"/></svg></button>
    </div>
  </header>

  <div class="navrow">
    <div class="shopby">Shop by category</div>
    <div class="tabs">
      <a href="#"><span class="ic">$</span>Online Special</a>
      <a href="#" style="border:0"><span class="ic">★</span>Favourite</a>
    </div>
  </div>

  <ul class="sidebar">
    <li>Baby</li><li>Bakery</li><li>Baking needs</li><li>Beverages</li><li>Biscuits</li><li>Breakfast foods</li><li>Canned foods</li><li>Cheese</li><li>Chilled foods</li><li>Chips</li><li>Condiments</li><li>Confectionery</li><li>Cooking needs</li><li>Desserts</li><li>Frozen foods</li><li>Fruit</li><li>Hardware and Outdoor</li><li>Health foods</li><li>Homewares</li><li>Household cleaning</li><li>International foods</li><li>Jams and Spreads</li><li>Laundary</li><li>Meat</li><li>Milk</li><li>Packet food</li><li>Pet care</li><li>Serviced Deli</li><li>Snacks</li><li>Soft drinks</li><li>Tissue products</li><li>Toiletries and Beauty</li><li>Vegetable</li>
  </ul>

  <div class="crumbs"><span>Home</span><span class="sep">&gt;&gt;</span><span>Fruits</span><span class="sep">&gt;&gt;</span><span class="here">Apples</span></div>

  <div class="card" style="left:159px;top:179px"><div class="photo" role="img" aria-label="Bag of red apples"></div><div class="title">Apple Red<small>2kg bag</small></div><div class="price">$8.39</div><div class="qty"><i>-</i>1<i>+</i></div><button class="add">ADD</button></div>
  <div class="card" style="left:319px;top:179px"><div class="photo" role="img" aria-label="Bag of red apples"></div><div class="title">Apple Red<small>2kg bag</small></div><div class="price">$8.39</div><div class="qty"><i>-</i>1<i>+</i></div><button class="add">ADD</button></div>
  <div class="card" style="left:479px;top:179px"><div class="photo" role="img" aria-label="Bag of red apples"></div><div class="title">Apple Red<small>2kg bag</small></div><div class="price">$8.39</div><div class="qty"><i>-</i>1<i>+</i></div><button class="add">ADD</button></div>
  <div class="card" style="left:160px;top:453px"><div class="photo" role="img" aria-label="Bag of red apples"></div><div class="title">Apple Red<small>2kg bag</small></div><div class="price">$8.39</div><div class="qty"><i>-</i>1<i>+</i></div><button class="add">ADD</button></div>
  <div class="card" style="left:320px;top:453px"><div class="photo" role="img" aria-label="Bag of red apples"></div><div class="title">Apple Red<small>2kg bag</small></div><div class="price">$8.39</div><div class="qty"><i>-</i>1<i>+</i></div><button class="add">ADD</button></div>
  <div class="card" style="left:480px;top:453px"><div class="photo" role="img" aria-label="Bag of red apples"></div><div class="title">Apple Red<small>2kg bag</small></div><div class="price">$8.39</div><div class="qty"><i>-</i>1<i>+</i></div><button class="add">ADD</button></div>

  <aside class="cart">
    <svg class="basket" width="22" height="20" viewBox="0 0 22 20"><path d="M6 8l5-6 5 6" fill="none" stroke="#e5252b" stroke-width="2"/><path d="M1 8h20l-3 11H4z" fill="#e5252b"/></svg>
    <div class="items">0 items</div>
    <div class="sub">Sub total<b>$0.00</b></div>
    <button class="checkout">Check out</button>
    <hr>
    <div class="collect">
      <div class="row"><svg width="12" height="16" viewBox="0 0 12 16"><path d="M6 0a4 4 0 0 1 4 4c0 3-4 6-4 6S2 7 2 4a4 4 0 0 1 4-4z" fill="#e5252b"/><rect x="1" y="11" width="10" height="5" rx="2" fill="#e5252b"/></svg>Click and Collect</div>
      <p>12/40 Marlow Street Easthaven TAS 7300</p>
      <div class="row"><svg width="18" height="14" viewBox="0 0 18 14"><rect x="0" y="2" width="11" height="8" fill="#e5252b"/><path d="M11 5h4l3 3v2h-7z" fill="#e5252b"/><circle cx="4" cy="12" r="2" fill="#e5252b"/><circle cx="14" cy="12" r="2" fill="#e5252b"/></svg>Delivery Info</div>
    </div>
  </aside>

  <footer class="footer">
    <h4 style="left:21px;top:20px">Download our app</h4>
    <div class="store" style="left:20px;width:123px"><span class="sq"></span>Appdeck</div>
    <div class="store" style="left:157px;width:128px"><span class="sq"></span>Storefront</div>
    <h4 style="left:17px;top:125px">We accept</h4>
    <div class="pay" style="left:20px;color:#1a3a8f">Paycard</div>
    <div class="pay" style="left:86px;color:#e5252b;font-size:12px">Cardnet</div>
    <svg style="position:absolute;left:145px;top:145px" width="30" height="30"><circle cx="15" cy="15" r="14" fill="#c9a43a"/><circle cx="15" cy="15" r="9" fill="#3a3220"/></svg>

    <h4 style="left:338px;top:21px">Informational Links</h4>
    <ul class="flinks" style="left:339px"><li>My Account</li><li>My Past Orders</li><li>Online Specials</li><li>Everyday Specials</li><li>About Qlane</li><li>About Us</li></ul>
    <div class="divider"></div>
    <ul class="flinks" style="left:473px"><li>Delivery</li><li>FAQ</li><li>Privacy Policy</li><li>Terms &amp; Conditions</li><li>End User License Agreement</li></ul>

    <h4 style="left:640px;top:23px">Contact us</h4>
    <div class="contact-phone">1300 555 019</div>
    <h4 style="left:643px;top:72px">Socialise</h4>
    <div class="social" style="left:641px;background:#3b5a9a"></div>
    <div class="social" style="left:675px;background:#4fb0e6"></div>
    <div class="social" style="left:710px;background:#e35a3b"></div>
  </footer>
</div>
</body>
</html>
```